Info Graphic for Real Estate Company

We are Brimlo.com, a real estate company based in Hong Kong. We need a simple info graphic that helps our readers understand more about the property market here. The current topic we are discussing is the difference in the hong kong market in 1997 (market crash) versus the market today. We have very clear direction attached, all of the copy and creative direction. We just need someone to put it in layout! Please see attached :)

Target Market(s)

30-60 year olds; highly educated (investment bankers, lawyers)

Industry/Entity Type

Real Estate

Font styles to use
Other font styles liked:
• Open Sans and Oswald

Colors

Designer to choose colors to be used in the design.

Requirements
Must have
• The attached copy
Nice to have
• A similar design to the attached
Should not have
• colors that do not fall within our guidelines (attached)

```html
<!DOCTYPE html>
<html lang="en">
<head>
<meta charset="utf-8">
<title>Top 5 Differences Between 1997 vs Now</title>
<link href="https://fonts.googleapis.com/css2?family=Oswald:wght@300;400;500&family=Open+Sans:wght@400;600&display=swap" rel="stylesheet">
<style>
  :root {
    --page-bg: #e7e7e7;
    --teal-bright: #00c4bc;
    --teal-deep: #00868a;
    --aqua: #34cfd6;
    --slate: #464c4c;
    --grey-light: #d5d5d5;
    --grey-mid: #b9b9b9;
    --ink: #141c1c;
    --white: #ffffff;
    --mist: #e9fbfa;
    --logo-bg: #ebebeb;
  }
  * { margin: 0; padding: 0; box-sizing: border-box; }
  html, body { width: 849px; height: 1200px; overflow: hidden; background: var(--page-bg); }
  .infographic {
    position: relative; width: 849px; height: 1200px; overflow: hidden;
    background: var(--page-bg);
    font-family: "Open Sans", Arial, sans-serif; color: var(--ink);
  }
  .hero {
    position: absolute; left: 0; top: 0; width: 849px; height: 345px;
    background: linear-gradient(90deg, #4c6b3e 0%, #7c9a5c 30%, #a7b58c 55%, #d9e0e2 68%, #eef1f3 100%);
  }
  .hero-title {
    position: absolute; left: 0; top: 112px; width: 849px; text-align: center;
    font-family: "Oswald", Impact, sans-serif; font-weight: 500;
    font-size: 58px; line-height: 64px; color: var(--white); letter-spacing: -0.5px;
    text-transform: uppercase;
  }
  .intro-panel {
    position: absolute; left: 0; top: 345px; width: 373px; height: 408px;
    background: var(--teal-bright);
  }
  .intro-heading {
    position: absolute; left: 40px; top: 52px; width: 320px;
    font-family: "Oswald", Impact, sans-serif; font-weight: 300;
    font-size: 40px; line-height: 42px; color: var(--mist); text-transform: uppercase;
  }
  .brand-plate {
    position: absolute; left: 40px; top: 297px; width: 282px; height: 57px;
    background: var(--logo-bg); display: flex; align-items: center; justify-content: center; gap: 10px;
  }
  .brand-name { font-family: "Open Sans", Arial, sans-serif; font-weight: 400; font-size: 21px; letter-spacing: 2px; color: #333; }
  .brand-mark { width: 14px; height: 14px; background: var(--teal-deep); }
  .fact { position: absolute; padding: 0 24px; display: flex; flex-direction: column; justify-content: center; }
  .fact-title { font-weight: 600; font-size: 16px; line-height: 20px; }
  .fact-body { font-size: 13px; line-height: 16px; }
  .fact-body.small { font-size: 11px; line-height: 13.5px; }
  .fact--activity { left: 418px; top: 425px; width: 431px; height: 124px; background: var(--grey-light); padding-left: 31px; }
  .fact--rates { left: 418px; top: 588px; width: 431px; height: 111px; background: var(--teal-deep); padding-left: 22px; padding-right: 10px; }
  .fact--afford { left: 80px; top: 793px; width: 677px; height: 109px; background: var(--aqua); padding-left: 21px; }
  .fact--debt { left: 80px; top: 942px; width: 677px; height: 109px; background: var(--slate); color: var(--white); padding-left: 22px; }
  .fact--china { left: 80px; top: 1094px; width: 677px; height: 106px; background: var(--grey-mid); padding-left: 22px; justify-content: flex-start; padding-top: 10px; }
</style>
</head>
<body>
<main class="infographic">
  <div class="hero" role="img" aria-label="Photo of a white modern house among tropical palm trees"></div>
  <h1 class="hero-title">Top 5 Differences Between<br>1997 vs Now</h1>

  <section class="intro-panel">
    <h2 class="intro-heading">Expert analysis of why Hong Kong real estate will not crash like it did in 1997</h2>
    <div class="brand-plate"><span class="brand-name">Brimlo.com</span><span class="brand-mark"></span></div>
  </section>

  <section class="fact fact--activity">
    <h3 class="fact-title">Buying has not reached frenzied levels</h3>
    <p class="fact-body">Market activity remains close to historical averages<br>•15-year average (2002-2016) = 7,180 transactions/month<br>•10-year average (2007-2016) = 7,150 transactions/month</p>
  </section>

  <section class="fact fact--rates">
    <h3 class="fact-title">Interest rates are far from risky</h3>
    <p class="fact-body">Hong Kong interest rates are approximately 3% (even lower than the 4-5% in most global economies). Going into the crash of 1997, interest rates were over 9%</p>
  </section>

  <section class="fact fact--afford">
    <h3 class="fact-title">Affordability – a tale of two cities</h3>
    <p class="fact-body small" style="font-size:12px;line-height:15px">The average property in HK requires 19 years of average income, almost double what it was in 1997. Properties are much less affordable to the average citizen. However, all is not equal, with a lot of pent up demand from people who have held back as a result of government measures and accumulated wealth on the sidelines. The rich have also gotten richer.</p>
  </section>

  <section class="fact fact--debt">
    <h3 class="fact-title">Excess Debt?</h3>
    <p class="fact-body small" style="font-size:12px;line-height:15px">Housing crashes are almost always caused by overleveraging – people borrowing more than they could afford to support when buying a property. The HKMA reported that Hong Kong’s average loan-to-value ratio is 51%, lower than the 64% before the cooling measures were introduced. Other global markets typically operate at LTV ratios of 70% or more, and may approach 100% before a housing crash</p>
  </section>

  <section class="fact fact--china">
    <h3 class="fact-title">China – the elephant in the property market</h3>
    <p class="fact-body small">China is perhaps the most important difference between 1997 and 2017. At the time of the handover, China’s economy was just starting its meteoric rise with a GDP of just under US$1 trillion. Over the next 20 years it would grow to over US$11 trillion. There remains tremendous room for mainland Chinese investors to invest in Hong Kong. This did not exist in 1997.</p>
  </section>
</main>
</body>
</html>
```